Tall Gum Equipment Hire Business Card Design

Tall Gum Equipment Hire Pty Ltd

WET or DRY HIRE

Kestro T5-8 + attachments
Turf Cutter
Lawn mowers with catchers
Brushcutters
Blowers

We require a business card with the above information for a new equipment hire Company. Would like to see a redish/brown background or something to do with an Australian Red Dog (Cattle Dog) on the business card as our Logo - even some sort of watermark as a background.

Business

ABN: 71 382 915 206
17C Hollins Road Brindle Creek Qld 4791
PO Box 5817 Brindle Creek Qld 4791
PH: 0417362908 or 0438105724
Email: fastslash@coralnetmail.com

```html
<!DOCTYPE html>
<html lang="en">
<head>
<meta charset="utf-8">
<title>Tall Gum Equipment Hire – Business Card</title>
<link rel="stylesheet" href="https://fonts.googleapis.com/css2?family=Quicksand:wght@400;500&family=Open+Sans:wght@400&display=swap">
<style>
  :root {
    --page-bg: #e6e6e6;
    --card-white: #ffffff;
    --brand-red: #8b2a24;
    --band-red: #9a2a22;
    --panel-dark: #17181a;
    --panel-dark-edge: #26282b;
    --text-light: #f2f2f2;
    --mist: #d9d9d9;
  }
  * { box-sizing: border-box; margin: 0; padding: 0; }
  html, body {
    width: 1200px;
    height: 900px;
    overflow: hidden;
    background: var(--page-bg);
  }
  .card {
    position: absolute;
    left: 150px;
    top: 175px;
    width: 900px;
    height: 550px;
    border-radius: 36px;
    overflow: hidden;
    background: var(--card-white);
    box-shadow: 0 18px 40px rgba(0,0,0,0.18);
  }
  .card__mist {
    position: absolute;
    right: 0;
    top: 0;
    width: 340px;
    height: 290px;
    background: radial-gradient(circle at 55% 60%, var(--mist) 0%, rgba(217,217,217,0.55) 45%, rgba(255,255,255,0) 72%);
  }
  .brand {
    position: absolute;
    left: 60px;
    top: 40px;
    display: flex;
    align-items: center;
    gap: 26px;
  }
  .brand__disc {
    width: 210px;
    height: 210px;
    border-radius: 50%;
    background: var(--brand-red);
  }
  .brand__name {
    font-family: "Quicksand", sans-serif;
    font-weight: 500;
    color: var(--brand-red);
    line-height: 1;
  }
  .brand__name-main {
    display: block;
    font-size: 92px;
    letter-spacing: 1px;
  }
  .brand__name-sub {
    display: block;
    font-size: 27px;
    letter-spacing: 2px;
    margin-top: 6px;
    padding-left: 4px;
  }
  .card__band {
    position: absolute;
    left: 0;
    top: 290px;
    width: 100%;
    height: 16px;
    background: var(--band-red);
  }
  .card__panel {
    position: absolute;
    left: 0;
    top: 306px;
    width: 100%;
    height: 244px;
    background: linear-gradient(180deg, var(--panel-dark-edge) 0%, var(--panel-dark) 100%);
  }
  .contacts {
    position: absolute;
    left: 66px;
    top: 30px;
    list-style: none;
    font-family: "Open Sans", sans-serif;
    color: var(--text-light);
    font-size: 25px;
    line-height: 33px;
  }
  .contacts__item {
    display: flex;
    align-items: center;
    gap: 10px;
    white-space: nowrap;
  }
  .contacts__icon {
    width: 26px;
    height: 24px;
    flex: none;
    fill: var(--band-red);
  }
  .contacts__item--abn {
    font-size: 21px;
    padding-left: 36px;
  }
</style>
</head>
<body>
  <div class="card">
    <div class="card__mist" role="img" aria-label="Faint misty bushland backdrop"></div>

    <div class="brand">
      <div class="brand__disc"></div>
      <div class="brand__name">
        <span class="brand__name-main">Tall Gum</span>
        <span class="brand__name-sub">Equipment Hire Pty Ltd</span>
      </div>
    </div>

    <div class="card__band"></div>

    <div class="card__panel">
      <ul class="contacts">
        <li class="contacts__item">
          <svg class="contacts__icon" viewBox="0 0 26 24"><path d="M13 2 1 12h4v10h6v-6h4v6h6V12h4z"/></svg>
          17C Hollins Road Brindle Creek Qld 4791
        </li>
        <li class="contacts__item">
          <svg class="contacts__icon" viewBox="0 0 26 24"><path d="M13 2 1 12h4v10h6v-6h4v6h6V12h4z"/></svg>
          PO Box 5817 Brindle Creek Qld 4791
        </li>
        <li class="contacts__item">
          <svg class="contacts__icon" viewBox="0 0 26 24"><path d="M6 3c1-1 2-1 3 0l3 4c.6.8.4 1.6-.3 2.2l-1.5 1.2c1 2.2 2.6 3.9 4.8 5l1.3-1.5c.6-.7 1.5-.8 2.2-.2l3.7 3c.9.8.9 1.9 0 2.7l-1.6 1.6c-1.3 1.3-3.4 1.5-5.4.5C9.6 19.5 5.5 15.4 3.5 9.8 2.8 7.8 3 5.800 4.3 4.5z"/></svg>
          0417362908
        </li>
        <li class="contacts__item">
          <svg class="contacts__icon" viewBox="0 0 26 24"><path d="M6 3c1-1 2-1 3 0l3 4c.6.8.4 1.6-.3 2.2l-1.5 1.2c1 2.2 2.6 3.9 4.8 5l1.3-1.5c.6-.7 1.5-.8 2.2-.2l3.7 3c.9.8.9 1.9 0 2.7l-1.6 1.6c-1.3 1.3-3.4 1.5-5.4.5C9.6 19.5 5.5 15.4 3.5 9.8 2.8 7.8 3 5.8 4.3 4.5z"/></svg>
          0438105724
        </li>
        <li class="contacts__item">
          <svg class="contacts__icon" viewBox="0 0 26 24"><path d="M2 8 13 2l11 6v14H2z"/><path d="M4 10l9 6 9-6" fill="none" stroke="#17181a" stroke-width="1.6"/></svg>
          fastslash@coralnetmail.com
        </li>
        <li class="contacts__item contacts__item--abn">ABN: 71 382 915 206</li>
      </ul>
    </div>
  </div>
</body>
</html>
```